Construction business card

We are a family run and family oriented business in Philadelphia and we are starting new. We proudly serve the public by giving our customers great work at affordable prices. We can do all aspects of construction from the roof to the basement. We would like our business card to incorporate tools and family.
Updates

Can y'all please incorporate a bulldog

Industry/Entity Type

Construction

Contact Information for Business Card

Harbor Builders LLC, Dennis Whitcomb, 1187 W 9th st Philadelphia Pa 19140, CEO Main phone (215) 555-0143 cellphone 215-555-0187 Dennis whitcomb Jr cellphone 267-555-0129 email harborbuildersllc@quillpost.example

Colors
f78f20
ffffff
1b1b1b

```html
<!DOCTYPE html>
<html lang="en">
<head>
<meta charset="utf-8">
<title>Harbor Builders LLC – Business Card</title>
<link href="https://fonts.googleapis.com/css2?family=Quicksand:wght@500;600;700&display=swap" rel="stylesheet">
<style>
  :root {
    --orange: #f78f20;
    --white: #ffffff;
    --ink: #1b1b1b;
    --charcoal: #3b3b3b;
    --backdrop: #e9e7e4;
  }
  * { box-sizing: border-box; margin: 0; padding: 0; }
  html, body {
    width: 1200px; height: 1000px; overflow: hidden;
    background: var(--backdrop);
    font-family: "Quicksand", sans-serif;
  }
  .card {
    position: absolute; left: 250px; width: 700px; height: 400px;
    border-radius: 40px; overflow: hidden;
    box-shadow: 0 10px 30px rgba(0,0,0,.18);
  }
  /* Front */
  .card-front {
    top: 60px;
    background: radial-gradient(ellipse at 50% 35%, var(--charcoal) 0%, #262626 55%, var(--ink) 100%);
  }
  .card-front .swoosh { position: absolute; left: 0; bottom: 0; width: 700px; height: 400px; }
  .brand {
    position: absolute; left: 0; right: 0; top: 150px;
    display: flex; align-items: center; justify-content: center; gap: 16px;
  }
  .brand-mark { width: 38px; height: 38px; background: var(--orange); border-radius: 4px; }
  .brand-name {
    color: var(--white); font-weight: 700; font-size: 44px; letter-spacing: 1px;
    text-transform: uppercase;
  }
  /* Back */
  .card-back { top: 540px; background: var(--white); color: var(--ink); }
  .back-brand {
    position: absolute; left: 36px; top: 36px;
    display: flex; align-items: center; gap: 8px;
  }
  .back-brand .brand-mark { width: 16px; height: 16px; border-radius: 2px; }
  .back-brand .brand-name { color: var(--orange); font-size: 18px; }
  .label { color: var(--orange); font-weight: 700; }
  .address {
    position: absolute; right: 44px; top: 52px; text-align: right;
    font-size: 22px; font-weight: 500; line-height: 1.25;
  }
  .address .label { font-size: 22px; margin-bottom: 4px; }
  .person { position: absolute; left: 50px; top: 238px; font-size: 22px; font-weight: 500; }
  .person .name { color: var(--orange); font-weight: 700; font-size: 30px; text-transform: uppercase; margin-bottom: 10px; }
  .line { display: flex; align-items: center; gap: 8px; line-height: 1.35; }
  .icon { width: 18px; height: 18px; flex: none; }
  .ceo {
    position: absolute; right: 44px; top: 272px; text-align: right;
    font-size: 24px; font-weight: 500;
  }
  .ceo .label { font-size: 30px; margin-bottom: 8px; }
  .ceo .line { justify-content: flex-end; }
</style>
</head>
<body>

<section class="card card-front">
  <svg class="swoosh" viewBox="0 0 700 400" aria-hidden="true">
    <path d="M0 400 L0 360 Q350 300 700 255 L700 400 Z" fill="#f78f20"/>
    <path d="M30 375 Q360 300 690 262 Q360 310 30 375 Z" fill="#ffffff" stroke="#ffffff" stroke-width="3"/>
  </svg>
  <div class="brand">
    <span class="brand-mark"></span>
    <span class="brand-name">Harbor Builders LLC</span>
  </div>
</section>

<section class="card card-back">
  <div class="back-brand">
    <span class="brand-mark"></span>
    <span class="brand-name">Harbor Builders LLC</span>
  </div>

  <div class="address">
    <div class="label">Address</div>
    <div>1187 W 9th st Philadelphia</div>
    <div>Pa 19140,</div>
  </div>

  <div class="person">
    <div class="name">Dennis Whitcomb</div>
    <div class="line">
      <svg class="icon" viewBox="0 0 18 18" aria-hidden="true"><rect x="4" y="1" width="10" height="16" rx="2" fill="none" stroke="#f78f20" stroke-width="2"/></svg>
      267-555-0129
    </div>
    <div class="line">
      <svg class="icon" viewBox="0 0 18 18" aria-hidden="true"><rect x="1" y="4" width="16" height="11" fill="none" stroke="#f78f20" stroke-width="1.6"/><path d="M1 4 L9 11 L17 4" fill="none" stroke="#f78f20" stroke-width="1.6"/></svg>
      harborbuildersllc@quillpost.example
    </div>
  </div>

  <div class="ceo">
    <div class="label">CEO</div>
    <div class="line">
      (215) 555-0143
      <svg class="icon" viewBox="0 0 18 18" aria-hidden="true"><path d="M4 2 L7 2 L8 6 L6 7.5 Q8 11 11 12.5 L12.5 10.5 L16 11.5 L16 15 Q9 16 2.5 8 Q2 4 4 2 Z" fill="#f78f20"/></svg>
    </div>
    <div class="line">
      215-555-0187
      <svg class="icon" viewBox="0 0 18 18" aria-hidden="true"><rect x="4" y="1" width="10" height="16" rx="2" fill="none" stroke="#f78f20" stroke-width="2"/></svg>
    </div>
  </div>
</section>

</body>
</html>
```